Mental Health Non-profit Website that takes donations

We are a faith friendly non profit mental health agency. We need an about us section, a section for taking donations, and a place to list all our therapists and a photo of them
Unfortunately, many of our neighbors in Ohio face mental health challenges which harm their quality of life. Thousands of Ohioans experience trauma, addiction, anxiety, and depression, and the negative outcomes of these experiences continue to grow. While we know that data-driven counseling can improve quality of life for those with mental health challenges, many face economic and social barriers to accessing this transformational care.
Lanterns of Calm crosses barriers to mental health care for Ohioans. We are a nonprofit team of counselors dedicated to employing best practices in modes accessible to people of all backgrounds. A trauma-informed, faith-sensitive methodology uniquely equips us to address holistic mental health challenges. Donor support and community partnerships allow us to meet and serve individuals who could not otherwise access professional care.

Please see our case for support below for more information.

Target Market(s)

Those seeking mental health therapy

Industry/Entity Type

Mental Health Non-profit

Coding

Coded - Design and coding required

Colors

Designer to choose colors to be used in the design.

Requirements
Must have
• Our logo colors of navy blue and gold, our logo, about us section, our mission section, a place to accept donations page for all of our therapists and their pictures, and a place for blog posts

```html
<!DOCTYPE html>
<html lang="en">
<head>
<meta charset="utf-8">
<title>Lanterns of Calm – Homepage Layouts</title>
<link rel="stylesheet" href="https://fonts.googleapis.com/css2?family=Dancing+Script:wght@700&family=Lexend:wght@400;500&family=Lato:wght@400;700&display=swap">
<style>
:root{
  --navy:#1b1a2f;--navy-2:#2a2840;--gold:#b08d1f;--gold-lt:#d6b23a;
  --cream:#f7f5ee;--gray:#cacacf;--ink:#232230;--muted:#4a4a55;
  --white:#fff;--board:#ebebee;
}
*{box-sizing:border-box;margin:0;padding:0}
html,body{width:1200px;height:2207px;overflow:hidden}
body{background:var(--board);position:relative;font-family:'Lato',sans-serif;color:var(--ink)}
.page{position:absolute;background:var(--cream);overflow:hidden;box-shadow:0 6px 24px rgba(0,0,0,.12)}
.page-a{left:38px;top:41px;width:530px;height:2106px}
.page-b{left:620px;top:41px;width:542px;height:2151px}
.abs{position:absolute}
.backdrop{position:absolute;left:0;top:0}
.photo{position:absolute;overflow:hidden}
.ornament{display:block;width:34px;height:4px;border-radius:50%;background:var(--gold);margin-bottom:6px}
.ornament.dark{background:var(--navy)}
.eyebrow{font-family:'Dancing Script',cursive;font-weight:700;color:var(--gold);font-size:15px;line-height:1.1}
.eyebrow.light{color:var(--white);font-size:19px}
.title{font-family:'Lexend',sans-serif;font-weight:400;font-size:14.5px;color:var(--ink);line-height:1.35;margin-top:3px}
.title.light{color:var(--white)}
.title.hero{font-size:19.5px;line-height:1.32;color:var(--white)}
.title.gold{color:var(--gold);font-weight:500}
.para{font-size:5.7px;line-height:2.4;color:var(--muted);margin-top:9px}
.para.light{color:#e8e6ef}
.btn{display:inline-block;font-family:'Lexend',sans-serif;font-size:5.8px;font-weight:500;letter-spacing:.2px;padding:5px 10px;border-radius:10px;margin-top:12px}
.btn-light{background:var(--white);color:var(--navy)}
.btn-gold{background:var(--gold);color:var(--white)}
/* nav */
.logo{position:absolute;display:flex;align-items:center;gap:4px;font-family:'Lexend',sans-serif;font-size:6px;color:var(--white)}
.logo-dot{width:9px;height:9px;border-radius:50%;background:var(--gold)}
.nav{position:absolute;top:20px;display:flex;align-items:center;gap:13px;font-family:'Lexend',sans-serif;font-size:6.2px;color:var(--white)}
.nav .active{color:var(--gold-lt)}
.nav .donate{background:var(--white);color:var(--navy);padding:5px 8px;border-radius:9px;font-size:5.8px;font-weight:500}
.nav-mark{position:absolute;top:4px;width:30px;height:4px;border-radius:50%;background:var(--gold-lt)}
.social-rail{position:absolute;display:flex;flex-direction:column;align-items:center;gap:4px}
.social-rail .line{width:1px;height:20px;background:var(--white);opacity:.7}
.ring{width:7px;height:7px;border-radius:50%;border:1px solid var(--white)}
/* cards */
.donate-card{position:absolute;background:var(--white);box-shadow:0 4px 14px rgba(0,0,0,.08);padding:20px 18px}
.donate-frame{position:absolute;border-left:3px solid var(--gold);border-bottom:3px solid var(--gold)}
.blog-big{position:absolute;background:var(--white);box-shadow:0 3px 10px rgba(0,0,0,.08)}
.blog-big .text{position:absolute;left:6px;right:6px;bottom:0;background:var(--white);padding:7px 9px}
.blog-small{position:absolute;background:var(--white);box-shadow:0 3px 10px rgba(0,0,0,.08);display:flex}
.blog-small .text{padding:9px 8px}
.date{display:inline-block;background:var(--navy);color:var(--white);font-size:4.6px;padding:2px 5px}
.blog-title{font-size:6.2px;color:var(--ink);margin-top:5px;line-height:1.3}
.blog-body{font-size:4.7px;color:var(--muted);margin-top:3px;line-height:1.55}
.therapist{position:absolute;background:var(--white);box-shadow:0 3px 10px rgba(0,0,0,.1);text-align:center;padding-top:68px}
.therapist.featured{border-bottom:2px solid var(--gold)}
.avatar{position:absolute;left:50%;top:-38px;width:90px;height:90px;margin-left:-45px;border-radius:50%;border:4px solid var(--gold);background:linear-gradient(160deg,#d9d4cc,#8c7f74)}
.avatar.bright{border-color:#f1c21b}
.t-name{font-family:'Lexend',sans-serif;font-size:7.2px;color:var(--ink)}
.t-role{font-size:5.6px;color:var(--muted);margin-top:4px}
.icon-row{display:flex;justify-content:center;gap:3px;margin-top:6px}
.icon-row span{width:8px;height:8px;border-radius:50%;border:1px solid var(--muted)}
.center-head{position:absolute;left:0;right:0;text-align:center}
.center-head .ornament{margin:0 auto 6px}
/* footer */
.footer-col{position:absolute;color:var(--white)}
.footer-title{font-family:'Lexend',sans-serif;font-size:14px;color:var(--white)}
.contact-row{display:flex;gap:10px;align-items:flex-start;margin-top:16px}
.contact-icon{width:13px;height:13px;border-radius:3px;background:var(--gold-lt);display:flex;align-items:center;justify-content:center}
.contact-label{font-family:'Lexend',sans-serif;font-size:7.5px}
.contact-value{font-size:7px;margin-top:4px}
.foot-social{display:flex;gap:5px;margin-top:20px}
.foot-social span{width:14px;height:14px;border-radius:50%;border:1.2px solid var(--gold-lt)}
.foot-links{list-style:none;margin-top:17px;padding-left:8px}
.foot-links li{font-size:6px;line-height:2.45}
.foot-logo{position:absolute;text-align:center;color:var(--gold-lt);font-family:'Lexend',sans-serif;font-size:11px}
.foot-logo .mark{width:60px;height:60px;border-radius:50%;background:var(--gold-lt);margin:0 auto 10px}
.copyright{position:absolute;font-size:6.8px;color:var(--white)}
.copyright em{font-style:normal;color:var(--gold-lt)}
</style>
</head>
<body>

<!-- ================= Layout A ================= -->
<section class="page page-a">
  <svg class="backdrop" width="530" height="2106" viewBox="0 0 530 2106" aria-hidden="true">
    <defs>
      <linearGradient id="a-hero" x1="0" x2="1" y1="0" y2="0">
        <stop offset="0" stop-color="#241f2c"/><stop offset=".55" stop-color="#8a6a1c"/><stop offset="1" stop-color="#2b2630"/>
      </linearGradient>
      <linearGradient id="a-goldband" x1="0" x2="1"><stop offset="0" stop-color="#b59420"/><stop offset="1" stop-color="#7d6517"/></linearGradient>
      <linearGradient id="a-grayband" x1="0" x2="1"><stop offset="0" stop-color="#b9b9bf"/><stop offset="1" stop-color="#dadade"/></linearGradient>
    </defs>
    <rect width="530" height="268" fill="url(#a-hero)"/>
    <path d="M0,395 C40,365 90,345 150,330 L150,570 C90,590 40,610 0,640 Z" fill="url(#a-goldband)"/>
    <path d="M60,380 C160,300 330,262 530,258 L530,472 C390,478 260,505 150,560 C120,570 90,470 60,380 Z" fill="var(--navy)"/>
    <path d="M0,985 C150,1085 350,1140 530,1150 L530,1373 C350,1370 150,1300 0,1210 Z" fill="url(#a-grayband)"/>
    <path d="M0,1880 C180,1848 400,1870 530,1960" fill="none" stroke="var(--navy)" stroke-width="3"/>
    <path d="M0,1895 C180,1862 400,1890 530,1985 L530,2106 L0,2106 Z" fill="var(--navy)"/>
  </svg>

  <div class="photo" role="img" aria-label="Smiling woman with eyes closed, enjoying fresh air" style="left:350px;top:50px;width:180px;height:218px;background:radial-gradient(ellipse at 55% 55%,#6b4a34 0,#6b4a34 30%,rgba(80,70,60,.2) 70%,transparent 75%)"></div>

  <div class="logo" style="left:20px;top:16px"><span class="logo-dot"></span>Lanterns of Calm</div>
  <span class="nav-mark" style="left:160px"></span>
  <nav class="nav" style="left:145px"><span class="active">Home</span><span>About us</span><span>Our mission</span><span>Accept donations</span><span>Our therapists</span><span>Blog</span><span class="donate">DONATE TODAY</span></nav>

  <div class="social-rail" style="left:27px;top:100px"><span class="line"></span><span class="ring"></span><span class="ring"></span><span class="ring"></span><span class="ring"></span><span class="ring"></span><span class="line"></span></div>

  <div class="abs" style="left:49px;top:90px;width:230px">
    <div class="eyebrow light">Welcome To</div>
    <h1 class="title hero">Lanterns of Calm<br>Behavioral Health</h1>
    <p class="para light">Mental health impacts every element of our daily lives. From the ways that we work to how we relate with our families.</p>
    <span class="btn btn-light">CASE FOR SUPPORT</span>
  </div>

  <div class="photo" role="img" aria-label="Counselor listening to a smiling young client" style="left:58px;top:311px;width:202px;height:202px;border-radius:50%;border:3px solid var(--gold);background:linear-gradient(135deg,#cfc3b0,#7e8fa6)"></div>
  <div class="abs" style="left:283px;top:310px;width:225px">
    <span class="ornament"></span>
    <div class="eyebrow">Introduction</div>
    <h2 class="title light">Lanterns of Calm Counseling</h2>
    <p class="para light">Mental health impacts every element of our daily lives. From the ways that we work to how we relate with our families, mental wellness allows us to be present in the moment and contribute positively to our communities.</p>
    <span class="btn btn-light">READ MORE</span>
  </div>

  <div class="donate-frame" style="left:76px;top:552px;width:310px;height:194px"></div>
  <div class="donate-card" style="left:80px;top:548px;width:308px;height:194px">
    <span class="ornament"></span>
    <div class="eyebrow">Donations</div>
    <h2 class="title">A Place To Accept Donations</h2>
    <p class="para" style="width:210px">Mental health impacts every element of our daily lives. From the ways that we work to how we relate with our families, mental wellness allows us to be present in the moment and contribute positively to our communities.</p>
    <span class="btn btn-gold">DONATE NOW</span>
  </div>
  <div class="photo" role="img" aria-label="Illustrated tree with leafy branches" style="left:331px;top:572px;width:163px;height:182px;border-radius:50% 50% 20% 20%;background:radial-gradient(circle at 50% 40%,#8b9d6a,#9c7b5e 60%,rgba(156,123,94,0) 72%)"></div>

  <div class="photo" role="img" aria-label="Counselor comforting a client" style="left:49px;top:803px;width:147px;height:120px;border-radius:6px;border-left:2px solid var(--gold);border-bottom:2px solid var(--gold);background:linear-gradient(135deg,#d8d5d0,#6b5a52)"></div>
  <div class="photo" role="img" aria-label="Group of older women talking outdoors" style="left:115px;top:889px;width:177px;height:124px;border-radius:6px;background:linear-gradient(135deg,#7c9064,#c4b7a2)"></div>
  <div class="abs" style="left:220px;top:805px;width:250px">
    <span class="ornament"></span>
    <div class="eyebrow">Our Mission</div>
    <h2 class="title">Introducing Lanterns of Calm</h2>
  </div>
  <div class="abs" style="left:304px;top:888px;width:180px">
    <p class="para">Lanterns of Calm crosses barriers to mental health care for Ohioans. We are a nonprofit team of counselors dedicated to employing best practices in modes accessible to people of all backgrounds. A trauma-informed, faith-sensitive methodology uniquely equips us to address holistic mental health challenges.</p>
    <span class="btn btn-gold">LEARN MORE</span>
  </div>

  <div class="photo" role="img" aria-label="Woman meditating cross-legged at home" style="left:289px;top:1137px;width:241px;height:236px;background:linear-gradient(160deg,#eeeae4,#9fb0cf 60%,#b79fcf)"></div>
  <div class="abs" style="left:49px;top:1090px;width:210px">
    <span class="ornament dark"></span>
    <div class="eyebrow" style="color:var(--navy)">Our Methodology</div>
    <h2 class="title gold">Mental health counseling</h2>
    <p class="para">Lanterns of Calm offers mental health counseling which leads our clients to build healthy relationships, set boundaries, and enjoy life again. We serve clients facing a broad range of mental health challenges, including addiction.</p>
    <span class="btn btn-gold">READ MORE</span>
  </div>

  <div class="abs" style="left:49px;top:1318px;width:300px">
    <span class="ornament"></span>
    <div class="eyebrow">Our Latest Blog</div>
    <h2 class="title">Approaches position Lanterns</h2>
  </div>
  <div class="blog-big" style="left:46px;top:1399px;width:222px;height:169px">
    <div class="photo" role="img" aria-label="Woman comforting a distressed man" style="left:0;top:0;width:222px;height:110px;background:linear-gradient(135deg,#8a6f5c,#6e7a5d)"></div>
    <div class="text">
      <span class="date">08/16/2024</span>
      <div class="blog-title">Lorem ipsum dolor sit amet, consectetur adipiscing elit</div>
      <div class="blog-body">Sed ut perspiciatis unde omnis iste natus error sit voluptatem accusantium doloremque laudantium, totam rem aperiam.</div>
    </div>
  </div>
  <div class="blog-small" style="left:275px;top:1399px;width:205px;height:79px">
    <div class="photo" role="img" aria-label="Two women in a counseling session" style="position:relative;width:88px;height:79px;background:linear-gradient(135deg,#cfcabf,#c9a94a)"></div>
    <div class="text"><span class="date">08/16/2024</span><div class="blog-title">Lorem ipsum dolor sit amet, consectetur.</div><div class="blog-body">Sed ut perspiciatis unde omnis iste natus error sit voluptatem accusantium doloremque laudantium.</div></div>
  </div>
  <div class="blog-small" style="left:275px;top:1489px;width:205px;height:79px">
    <div class="photo" role="img" aria-label="Calm woman with hands on chest" style="position:relative;width:88px;height:79px;background:linear-gradient(135deg,#b7552f,#6e3c2b)"></div>
    <div class="text"><span class="date">08/16/2024</span><div class="blog-title">Lorem ipsum dolor sit amet, consectetur.</div><div class="blog-body">Sed ut perspiciatis unde omnis iste natus error sit voluptatem accusantium doloremque laudantium.</div></div>
  </div>

  <div class="center-head" style="top:1618px">
    <span class="ornament"></span>
    <div class="eyebrow">Our Therapists</div>
    <h2 class="title">How We Create Access to Counseling</h2>
  </div>
  <div class="therapist" style="left:50px;top:1727px;width:133px;height:113px"><div class="avatar" role="img" aria-label="Portrait of therapist"></div><div class="t-name">Elena Hart</div><div class="t-role">Co-Founder &amp; CEO</div><div class="icon-row"><span></span><span></span><span></span><span></span><span></span></div></div>
  <div class="therapist featured" style="left:199px;top:1727px;width:133px;height:113px"><div class="avatar bright" role="img" aria-label="Portrait of therapist"></div><div class="t-name">Elena Hart</div><div class="t-role">Co-Founder &amp; CEO</div><div class="icon-row"><span></span><span></span><span></span><span></span><span></span></div></div>
  <div class="therapist" style="left:348px;top:1727px;width:133px;height:113px"><div class="avatar" role="img" aria-label="Portrait of therapist"></div><div class="t-name">Elena Hart</div><div class="t-role">Co-Founder &amp; CEO</div><div class="icon-row"><span></span><span></span><span></span><span></span><span></span></div></div>

  <div class="footer-col" style="left:49px;top:1920px">
    <div class="footer-title">Contact us</div>
    <div class="contact-row"><span class="contact-icon"><svg width="8" height="8" viewBox="0 0 24 24"><path d="M6.6 10.8a15 15 0 0 0 6.6 6.6l2.2-2.2a1 1 0 0 1 1-.25 11.4 11.4 0 0 0 3.6.6 1 1 0 0 1 1 1V20a1 1 0 0 1-1 1A17 17 0 0 1 3 4a1 1 0 0 1 1-1h3.5a1 1 0 0 1 1 1c0 1.25.2 2.45.6 3.6a1 1 0 0 1-.25 1z" fill="var(--navy)"/></svg></span><div><div class="contact-label">PHONE</div><div class="contact-value">(555) 014-2290</div></div></div>
    <div class="contact-row"><span class="contact-icon"><svg width="8" height="8" viewBox="0 0 24 24"><path d="M2 5h20v14H2z" fill="none" stroke="var(--navy)" stroke-width="2"/><path d="M2 5l10 8 10-8" fill="none" stroke="var(--navy)" stroke-width="2"/></svg></span><div><div class="contact-label">E-MAIL</div><div class="contact-value">hello@lanternsofcalm.org</div></div></div>
    <div class="foot-social"><span></span><span></span><span></span><span></span><span></span></div>
  </div>
  <div class="footer-col" style="left:226px;top:1920px">
    <div class="footer-title">Contact us</div>
    <ul class="foot-links"><li>Home</li><li>About us</li><li>Our mission</li><li>Accept donations</li><li>Our therapists</li><li>Blog</li><li>Contact Us</li></ul>
  </div>
  <div class="foot-logo" style="left:355px;top:1975px;width:135px"><div class="mark"></div>LANTERNS OF CALM</div>
  <p class="copyright" style="left:49px;top:2086px">© 2024 <em>Lanterns of Calm Behavioral Health.</em> All rights reserved.</p>
</section>

<!-- ================= Layout B ================= -->
<section class="page page-b">
  <svg class="backdrop" width="542" height="2151" viewBox="0 0 542 2151" aria-hidden="true">
    <defs>
      <linearGradient id="b-hero" x1="0" x2="1"><stop offset="0" stop-color="#1e1c33"/><stop offset=".6" stop-color="#2c2a3e"/><stop offset="1" stop-color="#4d5a3a"/></linearGradient>
      <linearGradient id="b-goldband" x1="0" x2="1"><stop offset="0" stop-color="#b59420"/><stop offset="1" stop-color="#7d6517"/></linearGradient>
      <linearGradient id="b-grayband" x1="0" x2="1"><stop offset="0" stop-color="#b9b9bf"/><stop offset="1" stop-color="#dadade"/></linearGradient>
    </defs>
    <rect width="542" height="283" fill="url(#b-hero)"/>
    <path d="M0,650 C40,625 90,605 150,590 L150,860 C90,880 40,900 0,930 Z" fill="url(#b-goldband)"/>
    <path d="M60,640 C180,590 360,562 542,557 L542,816 C400,822 270,850 150,900 C120,910 90,750 60,640 Z" fill="var(--navy)"/>
    <path d="M0,1005 C150,1110 360,1165 542,1180 L542,1403 C360,1400 150,1330 0,1240 Z" fill="url(#b-grayband)"/>
    <path d="M0,1922 C180,1898 400,1925 542,2010 L542,2151 L0,2151 Z" fill="var(--navy)"/>
  </svg>

  <div class="photo" role="img" aria-label="Smiling woman looking up outdoors" style="left:340px;top:40px;width:202px;height:243px;background:radial-gradient(ellipse at 50% 55%,#7a5a44 0,#7a5a44 30%,rgba(110,125,90,.3) 70%,transparent 78%)"></div>

  <div class="logo" style="left:50px;top:16px"><span class="logo-dot"></span>Lanterns of Calm</div>
  <span class="nav-mark" style="left:162px"></span>
  <nav class="nav" style="left:147px"><span class="active">Home</span><span>About us</span><span>Our mission</span><span>Accept donations</span><span>Our therapists</span><span>Blog</span><span class="donate">DONATE TODAY</span></nav>

  <div class="social-rail" style="left:25px;top:102px"><span class="line"></span><span class="ring"></span><span class="ring"></span><span class="ring"></span><span class="ring"></span><span class="ring"></span><span class="line"></span></div>

  <div class="abs" style="left:49px;top:92px;width:230px">
    <div class="eyebrow light">Welcome To</div>
    <h1 class="title hero">Lanterns of Calm<br>Behavioral Health</h1>
    <p class="para light">Mental health impacts every element of our daily lives. From the ways that we work to how we relate with our families.</p>
    <span class="btn btn-light">CASE FOR SUPPORT</span>
  </div>

  <div class="donate-frame" style="left:55px;top:323px;width:323px;height:197px"></div>
  <div class="donate-card" style="left:59px;top:319px;width:319px;height:197px">
    <span class="ornament"></span>
    <div class="eyebrow">Donations</div>
    <h2 class="title">A Place To Accept Donations</h2>
    <p class="para" style="width:220px">Mental health impacts every element of our daily lives. From the ways that we work to how we relate with our families, mental wellness allows us to be present in the moment and contribute positively to our communities.</p>
    <span class="btn btn-gold">DONATE NOW</span>
  </div>
  <div class="photo" role="img" aria-label="Illustrated tree with leafy branches" style="left:318px;top:340px;width:167px;height:189px;border-radius:50% 50% 20% 20%;background:radial-gradient(circle at 50% 40%,#8b9d6a,#9c7b5e 60%,rgba(156,123,94,0) 72%)"></div>

  <div class="photo" role="img" aria-label="Counselor listening to a smiling young client" style="left:57px;top:608px;width:210px;height:210px;border-radius:50%;border:3px solid var(--gold);background:linear-gradient(135deg,#cfc3b0,#7e8fa6)"></div>
  <div class="abs" style="left:290px;top:610px;width:230px">
    <span class="ornament"></span>
    <div class="eyebrow">Introduction</div>
    <h2 class="title light">Lanterns of Calm Counseling</h2>
    <p class="para light">Mental health impacts every element of our daily lives. From the ways that we work to how we relate with our families, mental wellness allows us to be present in the moment and contribute positively to our communities.</p>
    <span class="btn btn-light">READ MORE</span>
  </div>

  <div class="photo" role="img" aria-label="Counselor comforting a client" style="left:98px;top:886px;width:149px;height:100px;border-radius:6px;border-left:2px solid var(--gold);border-bottom:2px solid var(--gold);background:linear-gradient(135deg,#d8d5d0,#6b5a52)"></div>
  <div class="photo" role="img" aria-label="Group of older women talking outdoors" style="left:164px;top:975px;width:167px;height:126px;border-radius:6px;background:linear-gradient(135deg,#7c9064,#c4b7a2)"></div>
  <div class="abs" style="left:344px;top:860px;width:170px">
    <span class="ornament"></span>
    <div class="eyebrow">Our Mission</div>
    <h2 class="title">Introducing Lanterns</h2>
    <p class="para">Lanterns of Calm crosses barriers to mental health care for Ohioans. We are a nonprofit team of counselors dedicated to employing best practices in modes accessible to people of all backgrounds. A trauma-informed, faith-sensitive methodology uniquely equips us to address holistic mental health challenges. Donor support and community partnerships allow us to meet and serve individuals who could not otherwise access professional care.</p>
    <span class="btn btn-gold">LEARN MORE</span>
  </div>

  <div class="photo" role="img" aria-label="Woman meditating cross-legged at home" style="left:271px;top:1159px;width:271px;height:244px;background:linear-gradient(160deg,#eeeae4,#9fb0cf 60%,#b79fcf)"></div>
  <div class="abs" style="left:50px;top:1114px;width:215px">
    <span class="ornament dark"></span>
    <div class="eyebrow" style="color:var(--navy)">Our Methodology</div>
    <h2 class="title gold">Mental health counseling</h2>
    <p class="para">Lanterns of Calm offers mental health counseling which leads our clients to build healthy relationships, set boundaries, and enjoy life again. We serve clients facing a broad range of mental health challenges, including addiction.</p>
    <span class="btn btn-gold">READ MORE</span>
  </div>

  <div class="abs" style="left:50px;top:1348px;width:300px">
    <span class="ornament"></span>
    <div class="eyebrow">Our Latest Blog</div>
    <h2 class="title">Approaches position Lanterns</h2>
  </div>
  <div class="blog-big" style="left:47px;top:1429px;width:226px;height:174px">
    <div class="photo" role="img" aria-label="Woman comforting a distressed man" style="left:0;top:0;width:226px;height:114px;background:linear-gradient(135deg,#8a6f5c,#6e7a5d)"></div>
    <div class="text">
      <span class="date">08/16/2024</span>
      <div class="blog-title">Lorem ipsum dolor sit amet, consectetur adipiscing elit</div>
      <div class="blog-body">Sed ut perspiciatis unde omnis iste natus error sit voluptatem accusantium doloremque laudantium, totam rem aperiam.</div>
    </div>
  </div>
  <div class="blog-small" style="left:284px;top:1429px;width:209px;height:82px">
    <div class="photo" role="img" aria-label="Two women in a counseling session" style="position:relative;width:90px;height:82px;background:linear-gradient(135deg,#cfcabf,#c9a94a)"></div>
    <div class="text"><span class="date">08/16/2024</span><div class="blog-title">Lorem ipsum dolor sit amet, consectetur.</div><div class="blog-body">Sed ut perspiciatis unde omnis iste natus error sit voluptatem accusantium doloremque laudantium.</div></div>
  </div>
  <div class="blog-small" style="left:284px;top:1520px;width:209px;height:83px">
    <div class="photo" role="img" aria-label="Calm woman with hands on chest" style="position:relative;width:90px;height:83px;background:linear-gradient(135deg,#b7552f,#6e3c2b)"></div>
    <div class="text"><span class="date">08/16/2024</span><div class="blog-title">Lorem ipsum dolor sit amet, consectetur.</div><div class="blog-body">Sed ut perspiciatis unde omnis iste natus error sit voluptatem accusantium doloremque laudantium.</div></div>
  </div>

  <div class="center-head" style="top:1653px">
    <span class="ornament"></span>
    <div class="eyebrow">Our Therapists</div>
    <h2 class="title">How We Create Access to Counseling</h2>
  </div>
  <div class="therapist" style="left:51px;top:1765px;width:136px;height:114px"><div class="avatar" role="img" aria-label="Portrait of therapist"></div><div class="t-name">Elena Hart</div><div class="t-role">Co-Founder &amp; CEO</div><div class="icon-row"><span></span><span></span><span></span><span></span><span></span></div></div>
  <div class="therapist featured" style="left:203px;top:1765px;width:136px;height:114px"><div class="avatar bright" role="img" aria-label="Portrait of therapist"></div><div class="t-name">Elena Hart</div><div class="t-role">Co-Founder &amp; CEO</div><div class="icon-row"><span></span><span></span><span></span><span></span><span></span></div></div>
  <div class="therapist" style="left:356px;top:1765px;width:136px;height:114px"><div class="avatar" role="img" aria-label="Portrait of therapist"></div><div class="t-name">Elena Hart</div><div class="t-role">Co-Founder &amp; CEO</div><div class="icon-row"><span></span><span></span><span></span><span></span><span></span></div></div>

  <div class="footer-col" style="left:50px;top:1962px">
    <div class="footer-title">Contact us</div>
    <div class="contact-row"><span class="contact-icon"><svg width="8" height="8" viewBox="0 0 24 24"><path d="M6.6 10.8a15 15 0 0 0 6.6 6.6l2.2-2.2a1 1 0 0 1 1-.25 11.4 11.4 0 0 0 3.6.6 1 1 0 0 1 1 1V20a1 1 0 0 1-1 1A17 17 0 0 1 3 4a1 1 0 0 1 1-1h3.5a1 1 0 0 1 1 1c0 1.25.2 2.45.6 3.6a1 1 0 0 1-.25 1z" fill="var(--navy)"/></svg></span><div><div class="contact-label">PHONE</div><div class="contact-value">(555) 014-2290</div></div></div>
    <div class="contact-row"><span class="contact-icon"><svg width="8" height="8" viewBox="0 0 24 24"><path d="M2 5h20v14H2z" fill="none" stroke="var(--navy)" stroke-width="2"/><path d="M2 5l10 8 10-8" fill="none" stroke="var(--navy)" stroke-width="2"/></svg></span><div><div class="contact-label">E-MAIL</div><div class="contact-value">hello@lanternsofcalm.org</div></div></div>
    <div class="foot-social"><span></span><span></span><span></span><span></span><span></span></div>
  </div>
  <div class="footer-col" style="left:232px;top:1962px">
    <div class="footer-title">Contact us</div>
    <ul class="foot-links"><li>Home</li><li>About us</li><li>Our mission</li><li>Accept donations</li><li>Our therapists</li><li>Blog</li><li>Contact Us</li></ul>
  </div>
  <div class="foot-logo" style="left:362px;top:2015px;width:140px"><div class="mark"></div>LANTERNS OF CALM</div>
  <p class="copyright" style="left:50px;top:2131px">© 2024 <em>Lanterns of Calm Behavioral Health.</em> All rights reserved.</p>
</section>

</body>
</html>
```